Marrowbeck Dance Festival Association

We need a design for a pull up banner for the dance festival. The festival takes place every year and aims to encourage dancers in the local area to perform. Dancers are judged on their performance the genres include ballet, jazz, tap and hip hop.
The banner will be 850mm x 2000mm. .ai files will be required.
We have no current logo - a new logo can be included as part of the design. Please do not include the year as it is a banner we would use over several years. We are looking for bright attractive colours - preferably with a reflection of the different genres. One suggestion was to include silhouettes of the different genres (in colour) but other suggestions are welcome.
Festival

```html
<!DOCTYPE html>
<html lang="en">
<head>
<meta charset="utf-8">
<title>Marrowbeck Dance Festival – Pull Up Banner</title>
<link rel="stylesheet" href="https://fonts.googleapis.com/css2?family=Metamorphous&family=Lobster&family=Poiret+One&family=Fresca&display=swap">
<style>
  :root {
    --sky-top: #2a6a86;
    --sky-mid: #3b7e98;
    --sky-deep: #163f52;
    --dancer-shade: #0c2733;
    --stage-pink: #d02a64;
    --stage-dark: #4a0c26;
    --night: #000000;
    --paper: #ffffff;
    --shelf-top: #ffffff;
    --shelf-edge: #c9c9c9;
    --title-pink: #f0287a;
    --title-mid: #a8134c;
    --title-wine: #3e061c;
    --title-glow: #6fd8ff;
    --ink: #111111;
    --ballet: #ff5b5b;
    --jazz: #f3f04a;
    --tap: #6cff5c;
    --hiphop: #5cd6f7;
    --mark: #16303c;
  }
  * { margin: 0; padding: 0; box-sizing: border-box; }
  html, body { width: 1200px; height: 900px; overflow: hidden; background: var(--paper); }
  .sheet { position: relative; width: 1200px; height: 900px; }

  .banner { position: absolute; left: 0; top: 0; width: 1200px; height: 510px; overflow: hidden; background: var(--night); }
  .banner-backdrop {
    position: absolute; inset: 0 0 70px 0;
    background:
      radial-gradient(ellipse 40% 35% at 78% 18%, rgba(170,190,200,.45), transparent 70%),
      linear-gradient(180deg, var(--sky-mid) 0%, var(--sky-top) 30%, var(--sky-deep) 60%, var(--stage-pink) 86%, var(--stage-dark) 100%);
  }
  .dancers {
    position: absolute; left: 0; top: 90px; width: 1200px; height: 320px;
    background:
      radial-gradient(ellipse 9% 45% at 69% 55%, rgba(8,26,36,.95), transparent 75%),
      radial-gradient(ellipse 7% 35% at 27% 45%, rgba(8,26,36,.85), transparent 75%),
      radial-gradient(ellipse 6% 30% at 53% 50%, rgba(8,26,36,.75), transparent 75%),
      radial-gradient(ellipse 6% 32% at 12% 55%, rgba(8,26,36,.7), transparent 75%),
      radial-gradient(ellipse 5% 30% at 91% 50%, rgba(8,26,36,.75), transparent 75%),
      radial-gradient(ellipse 5% 26% at 42% 55%, rgba(8,26,36,.6), transparent 75%);
  }
  .crowd {
    position: absolute; left: 0; right: 0; top: 380px; height: 70px;
    background: linear-gradient(180deg, rgba(0,0,0,0) 0%, rgba(0,0,0,.75) 40%, var(--night) 75%);
  }

  .org { position: absolute; left: 30px; top: 28px; display: flex; align-items: center; gap: 26px; }
  .org-mark { width: 122px; height: 122px; border-radius: 50%; background: var(--mark); flex: none; }
  .org-name { display: block; }

  .shelf {
    position: absolute; left: 150px; top: 323px; width: 900px; height: 45px;
    background: linear-gradient(180deg, var(--shelf-top) 0%, var(--shelf-top) 62%, var(--shelf-edge) 64%, #b5b5b5 100%);
    clip-path: polygon(2% 0, 98% 0, 100% 62%, 100% 100%, 0 100%, 0 62%);
  }
  .title { position: absolute; left: 200px; top: 248px; }

  .genres { position: absolute; left: 0; right: 0; top: 452px; height: 48px; list-style: none;
    font-family: "Poiret One", sans-serif; font-size: 39px; }
  .genres li { position: absolute; transform: translateX(-50%); white-space: nowrap; -webkit-text-stroke: 1.2px currentColor; }
  .genre-ballet { left: 197px; color: var(--ballet); }
  .genre-jazz { left: 467px; color: var(--jazz); }
  .genre-tap { left: 728px; color: var(--tap); }
  .genre-hiphop { left: 1000px; color: var(--hiphop); }

  .detail { position: absolute; left: 18px; top: 527px; width: 360px; height: 360px; border-radius: 50%; overflow: hidden;
    background:
      radial-gradient(ellipse 30% 40% at 40% 10%, rgba(8,26,36,.6), transparent 75%),
      linear-gradient(180deg, #2f6f88 0%, #1f5166 55%, #17394a 74%, #b02a58 86%, #5a0e2c 100%); }
  .detail-shelf { position: absolute; left: 0; right: 0; top: 278px; height: 28px;
    background: linear-gradient(180deg, #ffffff 0%, #d2d2d2 100%); }
  .detail-title { position: absolute; left: 0; top: 60px; }

  .quality { position: absolute; left: 430px; top: 592px; width: 710px; text-align: center;
    font-family: "Fresca", sans-serif; font-size: 45px; line-height: 60px; color: var(--ink); }
</style>
</head>
<body>
<main class="sheet">
  <section class="banner">
    <div class="banner-backdrop" role="img" aria-label="Blue stage-light background with a dotted glow, fading to pink"></div>
    <div class="dancers" role="img" aria-label="Dark silhouettes of dancers in motion"></div>
    <div class="crowd" role="img" aria-label="Silhouetted festival crowd with raised hands"></div>

    <header class="org">
      <span class="org-mark"></span>
      <svg class="org-name" width="670" height="60" viewBox="0 0 670 60" aria-label="Marrowbeck Dance Festival Association">
        <text x="0" y="44" textLength="664" lengthAdjust="spacingAndGlyphs" font-family="Metamorphous, serif" font-size="40" fill="#ffffff" style="font-variant: small-caps">MARROWBECK DANCE FESTIVAL ASSOCIATION</text>
      </svg>
    </header>

    <div class="shelf"></div>
    <svg class="title" width="800" height="100" viewBox="0 0 800 100" aria-label="Marrowbeck Dance Festival">
      <defs>
        <linearGradient id="title-fill" x1="0" y1="0" x2="0" y2="1">
          <stop offset="0" stop-color="#f0287a"/>
          <stop offset=".5" stop-color="#a8134c"/>
          <stop offset="1" stop-color="#3e061c"/>
        </linearGradient>
        <filter id="title-glow" x="-10%" y="-30%" width="120%" height="160%">
          <feGaussianBlur stdDeviation="3"/>
        </filter>
      </defs>
      <g font-family="Lobster, cursive" font-size="72">
        <text x="27" y="77" textLength="746" lengthAdjust="spacingAndGlyphs" fill="#000" opacity=".75" filter="url(#title-glow)">Marrowbeck Dance Festival</text>
        <text x="25" y="70" textLength="750" lengthAdjust="spacingAndGlyphs" fill="none" stroke="#6fd8ff" stroke-width="12" stroke-linejoin="round" filter="url(#title-glow)">Marrowbeck Dance Festival</text>
        <text x="25" y="70" textLength="750" lengthAdjust="spacingAndGlyphs" fill="none" stroke="#ffffff" stroke-width="5" stroke-linejoin="round">Marrowbeck Dance Festival</text>
        <text x="25" y="70" textLength="750" lengthAdjust="spacingAndGlyphs" fill="url(#title-fill)">Marrowbeck Dance Festival</text>
      </g>
    </svg>

    <ul class="genres">
      <li class="genre-ballet">BALLET</li>
      <li class="genre-jazz">JAZZ</li>
      <li class="genre-tap">TAP</li>
      <li class="genre-hiphop">HIP HOP</li>
    </ul>
  </section>

  <figure class="detail" role="img" aria-label="Magnified detail of the festival title lettering and its glow">
    <div class="detail-shelf"></div>
    <svg class="detail-title" width="360" height="200" viewBox="0 0 360 200">
      <defs>
        <linearGradient id="detail-fill" x1="0" y1="0" x2="0" y2="1">
          <stop offset="0" stop-color="#f0287a"/>
          <stop offset=".5" stop-color="#a8134c"/>
          <stop offset="1" stop-color="#3e061c"/>
        </linearGradient>
        <filter id="detail-glow" x="-20%" y="-30%" width="140%" height="160%">
          <feGaussianBlur stdDeviation="5"/>
        </filter>
      </defs>
      <g font-family="Lobster, cursive" font-size="138">
        <text x="-30" y="170" fill="#000" opacity=".8" filter="url(#detail-glow)">e Danc</text>
        <text x="-34" y="156" fill="none" stroke="#6fd8ff" stroke-width="20" stroke-linejoin="round" filter="url(#detail-glow)">e Danc</text>
        <text x="-34" y="156" fill="none" stroke="#ffffff" stroke-width="8" stroke-linejoin="round">e Danc</text>
        <text x="-34" y="156" fill="url(#detail-fill)">e Danc</text>
      </g>
    </svg>
  </figure>

  <p class="quality">High Quality<br>You will see the effects after printing</p>
</main>
</body>
</html>
```